1 Page Website Design For Meadowline Rx Savings

~~I NEED A WEBSITE LANDING PAGE DESIGNED~~:

TITLE: GET UP TO 75% Off ALL YOUR DIABETIC SUPPLIES GUARANTEED
SUBITITLE: Never Pay Full Price For Your Diabetic Supplies Again!

~~FORM~~:
Choose Your Current Brand Of Diabetic Supplies That You Currently Use To See If They Are Covered Under Our Free Diabetic RX Assistance Program:

~~DROP DOWN MENU~~
Acarbose Up To 75% Off!

Verimbra Dux Up To 75% Off!

Verimbra Dux Xr Up To 54% Off!

Pelvo Up To 75% Off!

Borquell Up To 75% Off!

Tumisko Up To 75% Off!

Quisden Up To 75% Off!

Welvoke Up To 75% Off!

Zorpelline Up To 54% Off!

Zorpequin Up To 54% Off!

Zorpeta Up To 54% Off!

Calmivest Up To 75% Off!

Calmora Up To 75% Off!

Chlorpropamide Up To 75% Off!

Colesevelam Up To 75% Off!

Merrowin Up To 54% Off!

Qnrk Up To 75% Off!

Desmopressin 52% Off

Hostivel 74% Off

Pruntalex Up To 54% Off!
Sorvilk Up To 75% Off!

Delumbo Up To 75% Off!

Nuskavir Up To 75% Off!

Glimepiride 66% Off

Glipizide Up To 75% Off!

Glipizide Er Up To 75% Off!

Tremvalux Up To 75% Off!

Tremvalux Xr Up To 75% Off!

Brenzofil Up To 75% Off!

Brenzofil Xl Up To 75% Off!

Yestramor Up To 75% Off!

Kipolvan Up To 75% Off!

Glyburide Up To 75% Off!

Glyburide Micronized Up To 75% Off!
Ostrivel Up To 75% Off!

Pardow Up To 75% Off!

Vuntorek Up To 75% Off!

Restivon 50 50 Up To 75% Off!

Restivon Up To 75% Off!

Kavostra N Up To 75% Off!

Kavostra R Up To 75% Off!

Insulin Detemir Up To 75% Off!

Insulin Glulisine Up To 75% Off!

Pelsquorin Up To 75% Off!

Pelsquora Up To 75% Off!

Roblinex Up To 75% Off!

Roblinex Xr Up To 75% Off!

Roblivo Up To 75% Off!

Mespolure Up To 75% Off!

Wovrastelo Up To 75% Off!

Tilbemo Up To 75% Off!

Frastovane Xr Up To 75% Off!

Ovrink Up To 75% Off!

Sauprex Up To 75% Off!

Drunvelo Up To 54% Off!

Metformin 73% Off

Pastoquil Up To 54% Off!

Miglitol Up To 75% Off!

Ferbalick Up To 33% Off!

Nateglinide Up To 75% Off!

Ulvoria Up To 75% Off!

Zestrapol Up To 75% Off!

Zestrabin N Up To 75% Off!

Zestrabin R Up To 75% Off!

Zestrakor Up To 75% Off!

Zestraplum Up To 33% Off!

Brumvexa Up To 75% Off!

Tescavil Up To 54% Off!

Krudal Up To 75% Off!

Pioglitazone Up To 75% Off!

Pramlintide Up To 75% Off!

Wolbanix Up To 54% Off!

Wolbary Up To 75% Off!

Humbrek 20% Off

Repaglinide Up To 75% Off!

Sadvex Up To 75% Off!

Rosiglitazone Up To 75% Off!

Sitagliptin Up To 75% Off!

Plumvoy Up To 75% Off!

Garvostek Up To 75% Off!

Treskuvo Up To 75% Off!

Obrilcha Up To 75% Off!

Tolazamide Up To 75% Off!

Tolbutamide Up To 75% Off!

Vempruka Up To 54% Off!

Faskid Up To 75% Off!

Lurmobixa Up To 75% Off!

Qualmedo Up To 75% Off!

Sombrewick Up To 15% Off!

Vantoberry Up To 75% Off!

Dombrisel Up To 33% Off!

Harnupex Up To 75% Off!

Pidsarn Up To 75% Off!

Brafmel Xr Up To 75% Off!

~~~~After they choose one I want this message to pop up~~~~:

YES! ~~NAME OF DRUG~~ IS COVERED UNDER OUR FREE DIABETIC RX PROGRAM!
3 EASY WAYS TO RECEIVE YOUR FREE DIABETIC RX ASSISTANCE VOUCHER:

1. Simply Click Below To Download Your Voucher Right Now!

~~DOWNLOAD VOUCHER NOW~~
2. Enter Your Cell Phone Number And We Will Send The Voucher To You By Text Message Instantly:

3. Enter Your Email And We Will Send The Voucher To Your Email Instantly:

Target Market(s)

People with Diabetes

Number of Pages Required

1 page

Colors

Designer to choose colors to be used in the design.

Requirements
Must have
• must be professional looking and build trust and credibility
Nice to have
• Photos of diabetics...real people
Should not have
• red

```html
<!DOCTYPE html>
<html lang="en">
<head>
<meta charset="utf-8">
<title>Meadowline Rx Savings</title>
<link rel="stylesheet" href="https://fonts.googleapis.com/css2?family=Jost:wght@400;500&family=Open+Sans:wght@400;600&display=swap">
<style>
  :root {
    --teal: #1aacb4;
    --teal-deep: #0b7a80;
    --accent: #0e8a90;
    --header-bg: #f2f2f2;
    --nav-text: #555a5c;
    --brand-text: #3f4446;
    --footer-bg: #0e5157;
    --footer-text: #8fb3b6;
    --orange: #ff8c00;
    --white: #ffffff;
    --field-text: #8a8a8a;
    --list-bg: #f4f4f4;
    --list-line: #dddddd;
    --list-text: #666666;
    --dim: rgba(0, 0, 0, 0.62);
  }
  * { box-sizing: border-box; margin: 0; padding: 0; }
  html, body { width: 1200px; height: 932px; overflow: hidden; }
  body { position: relative; font-family: "Open Sans", sans-serif; background: #222; }

  .site-header {
    position: absolute; left: 0; top: 0; width: 1200px; height: 93px;
    background: var(--header-bg);
  }
  .brand {
    position: absolute; left: 116px; top: 19px;
    font-family: "Open Sans", sans-serif; font-weight: 600; font-size: 24px; line-height: 28px;
    color: var(--brand-text);
  }
  .main-nav { position: absolute; top: 32px; left: 0; width: 1200px; }
  .main-nav a {
    position: absolute; font-family: "Jost", sans-serif; font-size: 18px;
    color: var(--nav-text); text-decoration: none; white-space: nowrap;
  }
  .main-nav a.is-active { color: var(--accent); }

  .hero {
    position: absolute; left: 0; top: 93px; width: 1200px; height: 703px;
  }
  .hero-photo {
    position: absolute; inset: 0;
    background: linear-gradient(120deg, #c9b8a8 0%, #e9e4de 35%, #9fb8c2 60%, #3d6f86 80%, #d8c6b4 100%);
  }
  .hero-title {
    position: absolute; left: 0; top: 92px; width: 1200px; text-align: center;
    font-family: "Open Sans", sans-serif; font-weight: 600; font-size: 38px; letter-spacing: -0.5px;
    color: var(--white); white-space: nowrap;
  }
  .hero-title .accent { color: #1fc4cc; }

  .drug-list {
    position: absolute; left: 467px; top: 540px; width: 274px;
    background: var(--list-bg); border: 1px solid var(--list-line);
  }
  .drug-list li {
    list-style: none; height: 36px; line-height: 36px; padding-left: 34px;
    font-size: 12px; color: var(--list-text); border-top: 1px solid var(--list-line);
  }
  .drug-list li:first-child { border-top: none; }

  .site-footer {
    position: absolute; left: 0; top: 796px; width: 1200px; height: 136px;
    background: var(--footer-bg);
  }
  .footer-nav a {
    position: absolute; top: 41px; font-family: "Jost", sans-serif; font-size: 18px;
    color: var(--footer-text); text-decoration: none; white-space: nowrap;
  }
  .copyright {
    position: absolute; left: 118px; top: 78px; font-family: "Jost", sans-serif;
    font-size: 15px; color: var(--footer-text); white-space: nowrap;
  }
  .social { position: absolute; left: 918px; top: 40px; }

  .page-dim { position: absolute; inset: 0; background: var(--dim); }

  .voucher-modal {
    position: absolute; left: 116px; top: 234px; width: 937px; height: 399px;
    background: var(--teal); color: var(--white); text-align: center;
  }
  .modal-title {
    position: absolute; left: 0; top: 38px; width: 100%;
    font-weight: 400; font-size: 23px; line-height: 29px; letter-spacing: 0.2px;
  }
  .modal-sub {
    position: absolute; left: 0; top: 107px; width: 100%; font-size: 14.5px; letter-spacing: 0.1px;
  }
  .step { position: absolute; top: 152px; width: 280px; }
  .step-num {
    width: 51px; height: 51px; margin: 0 auto; border-radius: 50%;
    background: var(--teal-deep); font-size: 31px; line-height: 51px; font-weight: 400;
  }
  .step-num.is-plain { background: none; }
  .step p { margin-top: 6px; font-size: 15px; line-height: 25px; }
  .step-1 { left: 43px; }
  .step-2 { left: 327px; top: 156px; }
  .step-2 p { margin-top: 1px; }
  .step-3 { left: 616px; }
  .step-3 p { margin-top: 5px; }

  .btn-download {
    position: absolute; left: 79px; top: 297px; width: 222px; height: 46px;
    background: var(--orange); color: var(--white); border: none;
    font-family: "Jost", sans-serif; font-size: 18px; line-height: 46px;
  }
  .field {
    position: absolute; top: 301px; width: 222px; height: 37px;
    background: var(--white); padding-left: 20px; line-height: 37px; text-align: left;
    font-family: "Jost", sans-serif; color: var(--field-text);
  }
  .field-phone { left: 366px; font-size: 18px; letter-spacing: 0.5px; }
  .field-email { left: 645px; font-size: 15px; }
</style>
</head>
<body>
  <header class="site-header">
    <div class="brand">Meadowline<br>Rx Savings</div>
    <nav class="main-nav">
      <a class="is-active" style="left:477px">Home</a>
      <a style="left:561px">About Us</a>
      <a style="left:672px">Services</a>
      <a style="left:774px">Download</a>
      <a style="left:893px">Programs</a>
      <a style="left:1006px">Contact</a>
    </nav>
  </header>

  <section class="hero">
    <div class="hero-photo" role="img" aria-label="Photo of a caregiver checking an older person's blood sugar at home"></div>
    <h1 class="hero-title"><span class="accent">GET UP TO 75% OFF</span> ALL YOUR DIABETIC SUPPLIES</h1>
    <ul class="drug-list">
      <li>Delumbo Up To 75% Off!</li>
      <li>Nuskavir Up To 75% Off!</li>
      <li>Glimepiride 66% Off</li>
    </ul>
  </section>

  <footer class="site-footer">
    <nav class="footer-nav">
      <a style="left:118px">Home</a>
      <a style="left:205px">About Us</a>
      <a style="left:322px">Our Plans</a>
      <a style="left:441px">Benefits</a>
      <a style="left:546px">Apply</a>
      <a style="left:633px">Contact Us</a>
    </nav>
    <p class="copyright">© 2017 Company Name &nbsp;All right reserved &nbsp;Term of Use</p>
    <svg class="social" width="160" height="40" viewBox="0 0 160 40" aria-label="Social links">
      <circle cx="20" cy="19" r="17.5" fill="#4fa9c4" stroke="#123" stroke-width="1.5"/>
      <circle cx="60" cy="19" r="17.5" fill="#3b5b9a" stroke="#123" stroke-width="1.5"/>
      <circle cx="100" cy="19" r="17.5" fill="#2a7aa8" stroke="#123" stroke-width="1.5"/>
      <circle cx="139" cy="19" r="17.5" fill="#c0553f" stroke="#123" stroke-width="1.5"/>
    </svg>
  </footer>

  <div class="page-dim"></div>

  <div class="voucher-modal">
    <h2 class="modal-title">YES! ACARBOSE IS COVERED UNDER OUR<br>FREE DIABETIC RX PROGRAM!</h2>
    <p class="modal-sub">3 EASY WAYS TO RECEIVE YOUR FREE DIABETIC RX ASSISTANCE VOUCHER:</p>

    <div class="step step-1">
      <div class="step-num">1</div>
      <p>Simply Click Below To Download<br>Your Voucher Right Now!</p>
    </div>
    <div class="step step-2">
      <div class="step-num">2</div>
      <p>Enter Your Cell Phone Number And<br>We Will Send The Voucher To You<br>By Text Message Instantly:</p>
    </div>
    <div class="step step-3">
      <div class="step-num is-plain">3</div>
      <p>Enter Your Email And We Will<br>Send The Voucher To Your<br>Email Instantly:</p>
    </div>

    <button class="btn-download">Download Voucher Now</button>
    <div class="field field-phone">123-456-7890</div>
    <div class="field field-email">info@email.com</div>
  </div>
</body>
</html>
```